Flash Website Intro
Animated flash intro for existing website with skip to site button
Hi Mira,
I sent you a private message regarding the updated link of my entry. Thanks
Tobin
Thank you for all your great work
I will now go through them with my partner and will let you know the decision
thanks
@Project Holder
Please check your private message and view my animation please.
http://vexloop.example/serve/5517302
Thanks
RunaFeld
dear sir,
i send link in private message. in that some clarity missing but real one is crystal clear
Hi PH, I sent you 2 link for #9
I sent you the link via private message.
for my entry#7
Hi,
Have you seen the animated version of my entry #5? I sent you the link via private message.
It is against the t&c's to send email address.
If you can upload to the internet and send me a link to view animation.
I won't be able to pick a design just from a static screenshot so please send me a link to view the full animation
thanks,
it's possible to see the animated result but we need to have ur personnal e-mail cauz here we cannot upload file larger than 2 mb . that's why
I have another doubt, banner or intro web, because I do not close their sizes
.gif format work here.
Hi
I have asked support how I view the animation rather than just a screenshot. Haven't had a response yet.
If anyone knows how I can view the flash files before I choose one please let me know
Hey i few questions:
How can uploads the swf´s
Or you want to take a screencapture of the intro.
Thank u
Please ignore the "Ad Sizes Required:" in the brief as it is just one flash banner size 880 x 325 (same as the white box on the home page of the website)

```html
<!DOCTYPE html>
<html lang="en">
<head>
<meta charset="UTF-8">
<title>Brightfen — Intro</title>
<link rel="stylesheet" href="https://fonts.googleapis.com/css2?family=Arimo:wght@400&display=swap">
<style>
  :root {
    --burst-core: #ffffff;
    --burst-glow: #e4f1de;
    --green-light: #9cc88f;
    --green-mid: #6fa860;
    --green-deep: #3f7a33;
    --green-dark: #1c4a17;
    --name-colour: #ffffff;
    --button-bg: #2e2e2e;
    --button-text: #ffffff;
  }
  * { margin: 0; padding: 0; box-sizing: border-box; }
  html, body {
    width: 1200px;
    height: 478px;
    overflow: hidden;
    background: var(--green-dark);
  }
  .intro-stage {
    position: relative;
    width: 1200px;
    height: 478px;
    overflow: hidden;
  }
  .energy-backdrop {
    position: absolute;
    inset: 0;
    background:
      radial-gradient(ellipse 300px 230px at 540px 140px, var(--burst-core) 0%, rgba(255,255,255,0.9) 30%, rgba(228,241,222,0.45) 62%, rgba(228,241,222,0) 100%),
      radial-gradient(ellipse 700px 460px at 580px 170px, var(--burst-glow) 0%, var(--green-light) 35%, var(--green-mid) 55%, var(--green-deep) 80%, var(--green-dark) 100%);
  }
  .brand-name {
    position: absolute;
    left: 600px;
    top: 196px;
    font-family: "Arimo", sans-serif;
    font-weight: 400;
    font-size: 58px;
    line-height: 1;
    letter-spacing: 1px;
    color: var(--name-colour);
  }
  .skip-intro {
    position: absolute;
    left: 538px;
    top: 372px;
    width: 132px;
    height: 60px;
    display: flex;
    align-items: center;
    justify-content: center;
    background: var(--button-bg);
    color: var(--button-text);
    font-family: "Arimo", sans-serif;
    font-size: 15px;
    border: none;
    border-radius: 2px;
  }
</style>
</head>
<body>
  <main class="intro-stage">
    <div class="energy-backdrop" role="img" aria-label="Glowing green energy burst with branching lightning streaks radiating from a bright white center"></div>
    <h1 class="brand-name">Brightfen</h1>
    <button class="skip-intro" type="button">Skip Intro</button>
  </main>
</body>
</html>
```